15 ft high by 10 ft wide road side sign

road side sign - this is a dual carrigeway speeds of 40 mph so eye time to see ,read and absorb very short is less than 3 seconds 45,000 vehicles a day go past these are local to us our most profitable business is customers instore we embroider company and club and school logos and badges one mile ahead of this sign we have over 400,000 logos we have sewn and are on our servers we are well know in our area we can sew your logo in under 2 hours if it is already on our server we have a fast track service which we charge extra for very profitable is the customers buying items on tradora and bidlot we can really be fast on your own items if you bring them instore we have 15 large multi head machine to cope no one else is that fast on line embroidery takes 7 -10 days we have purchased from others saying 24 hours when put to the test they fail and give excusses why it cannot be do every time we have brought and our customers say the same project your logo embrodery one mile ahead ------- road side sign 15 ft high 10 feet wide company name Harrow Stitch & Embrodery 12 Corvel way EN4 7TR like drivers to be able to drop off and collect sameday because driving you have very very little time to read has to be simple good thing is its a major commutor route A10 Enfield so drivers can be trained via repeat reading dale fenwick

Target Market(s)

our local area is our most profitable market getting people instore online is to slow to for our custopmers and low a margin for us 1,000,000 people withing 2 miles of our store

Industry/Entity Type

Embroidery

Font styles to use
Sans Serif

Colors

Designer to choose colors to be used in the design.

Requirements
Must have
• simple easy to read
• also
• nigel pratley lovers he has NP sewn on his union jack boxer shorts
• as clothing with your company logo are 100% tax deductable for most companies
• as promotional wear
Should not have
• to complicated to read and understand so many people driving past are not english readers as there main language

```html
<!DOCTYPE html>
<html lang="en">
<head>
<meta charset="utf-8">
<title>Harrow Stitch &amp; Embrodery – Roadside Sign</title>
<link rel="stylesheet" href="https://fonts.googleapis.com/css2?family=Anton&display=swap">
<style>
  :root {
    --orange-light: #ff6a1a;
    --orange-deep: #f04e00;
    --white: #ffffff;
    --teal: #2fa3ab;
    --teal-dark: #1f7d86;
    --purple: #8a1a7a;
    --clock-gold: #f5b80c;
    --shirt-dark: #2a2a2c;
    --shirt-mid: #3a3a3d;
    --yellow: #fff200;
  }
  * { margin: 0; padding: 0; box-sizing: border-box; }
  html, body { width: 800px; height: 1200px; overflow: hidden; }
  body {
    font-family: "Anton", "Oswald", sans-serif;
    background: linear-gradient(160deg, var(--orange-light) 0%, var(--orange-deep) 100%);
  }
  .sign { position: relative; width: 800px; height: 1200px; overflow: hidden; }

  .headline {
    position: absolute;
    color: var(--white);
    text-transform: uppercase;
    line-height: 1;
    white-space: nowrap;
  }
  .headline--customize { left: 74px; top: 112px; font-size: 142px; letter-spacing: 1px; }
  .headline--items { left: 248px; top: 252px; font-size: 100px; }

  .speed-band { position: absolute; left: 262px; top: 352px; width: 460px; height: 140px; }
  .headline--time { left: 290px; top: 372px; font-size: 86px; }

  .stopwatch {
    position: absolute; left: 90px; top: 316px; width: 180px; height: 180px;
    border-radius: 50%;
    background: radial-gradient(circle, var(--clock-gold) 0 60%, var(--purple) 61% 100%);
  }

  .shirt {
    position: absolute; left: 0; top: 548px; width: 800px; height: 652px;
    background: linear-gradient(180deg, var(--shirt-mid), var(--shirt-dark));
    border-radius: 240px 240px 0 0;
  }

  .business { position: absolute; left: 0; right: 0; top: 780px; text-align: center; text-transform: uppercase; }
  .business__name { color: var(--yellow); font-size: 82px; line-height: 1.08; }
  .business__address { color: var(--white); font-size: 38px; margin-top: 10px; letter-spacing: 1px; }
</style>
</head>
<body>
<main class="sign">
  <div class="shirt" role="img" aria-label="Black t-shirt carrying the shop name"></div>

  <h1 class="headline headline--customize">Customize</h1>
  <p class="headline headline--items">Your items</p>

  <svg class="speed-band" viewBox="0 0 460 140" aria-hidden="true">
    <polygon points="0,118 455,96 455,122 0,140" fill="var(--purple)"/>
    <polygon points="10,14 455,0 455,96 10,118" fill="var(--teal)"/>
    <polygon points="10,14 455,0 455,10 10,24" fill="var(--teal-dark)"/>
  </svg>
  <p class="headline headline--time">Under 2hrs</p>

  <div class="stopwatch" role="img" aria-label="Stopwatch showing fast service"></div>

  <section class="business">
    <h2 class="business__name">Harrow Stitch &amp;<br>Embrodery</h2>
    <p class="business__address">12 Corvel Way, EN4 7TR</p>
  </section>
</main>
</body>
</html>
```